Web re-design project for web software development agency

We need to re-design our existing website (www.tovenmedia.co.uk), and are going to start using a shorter domain (www.toven.com).
We have been in business for 8 years and it's time for an update.

We are based at Harrowmede Court (home of the code breakers). We specialise in writing software for the web. Over the years we have built up a healthy customer base and it is time to incorporate the features we build for our customers into our own site (e.g. social media).

We have a team of 8 talented developers with varied skills including: apps for mobile; complex server side software; front-end software; eCommerce software; specialised web based applications; integration software; hardware support; consultancy services. Our customers are diverse (e.g. banking; commerce; veterinary; R&D; health sector; law; accounting; film industry etc.).

Our current colour scheme is blue, white and green although we are not averse to moving away from these colours. We will also be dropping the DESIGN from our name and logo. Revised logo will be attached.

The site needs to be modern, sophisticated and leading edge. We want to show visitors to the site that we are a professional organisation.
Updates

Our logo in PSD format has been uploaded. Please drop the word DESIGN from the logo.

The deliverable for this project is a PSD (ideally we would like to see how the home page, portfolio page, resources page with mugshots, and forms are going to look).

Many thanks,
Tom

Please DO NOT include a Careers section 

We will also need a "meet our team" section with spaces for 10 photographs as well as some space underneath them so that we can add a short paragraph for each one of them.

Target Market(s)

Mainly large corporations needing bespoke web software, or generally complex projects (for anyone).

Industry/Entity Type

Software

Requirements
Must have
• We would like a home page designed that has the following elements on it:
- Show the new cookie compliance policy displayed probably in the top of the page (will disappear).
- A client Testimonial.
- Pricing icon.
- Social media Links.
- A Quote section in expand/collapse field as in (http://www.quillbrook-online.co.uk/our-services.shtml)

We would also like a portfolio page that showcases our clients in an interesting way.

Finally, we would like a form design that we can use throughout the site (i.e. how should buttons, radio buttons, checkboxes, dropdowns, text areas etc. look)?
Nice to have
• A page that follows these guidelines:
http://www.pagerivet.com/the-anatomy-of-a-perfect-landing-page

Here are a few examples of sites in our sector that we like:
- http://www.tidewell-studio.com/
- http://plinthos.co.uk/
- http://www.fernaxis.com/services/web-development (nice contact us page)
- http://www.quillbrook-online.co.uk/
- http://www.lumsa.com/
- http://www.netmoxa.co.uk/
Should not have
• No flash elemets. If anything, we will use html5.

```html
<!DOCTYPE html>
<html lang="en">
<head>
<meta charset="utf-8">
<title>Toven – Web Design</title>
<link rel="stylesheet" href="https://fonts.googleapis.com/css2?family=Bree+Serif&family=Roboto:wght@300;400;500&family=Arimo:wght@400;700&display=swap">
<style>
:root{
  --ink:#2a2a2a;
  --header:#2e2e2e;
  --header-dark:#1f1f1f;
  --lime:#a9c41f;
  --lime-dark:#8aa216;
  --sky:#1f9fd8;
  --sky-light:#49bde9;
  --navy:#123a5c;
  --orange:#f47a22;
  --orange-light:#ff9a45;
  --link:#1b6aa5;
  --muted:#8a8a8a;
  --line:#dcdcdc;
  --paper:#f4f4f4;
  --white:#ffffff;
}
*{box-sizing:border-box;margin:0;padding:0}
html,body{width:1075px;height:1200px;overflow:hidden}
body{position:relative;background:var(--paper);font-family:"Roboto",Arial,sans-serif;color:var(--ink)}
.abs{position:absolute}
ul{list-style:none}

/* header */
.site-header{left:0;top:0;width:1075px;height:70px;background:linear-gradient(var(--header),var(--header-dark));border-bottom:1px solid #555}
.brand{left:136px;top:8px;display:flex;align-items:center;gap:8px}
.brand-square{width:28px;height:28px;background:var(--lime)}
.brand-name{font-family:"Arimo",sans-serif;font-weight:700;font-size:26px;color:var(--white);letter-spacing:1px}
.main-nav{left:426px;top:26px;display:flex;gap:16px;align-items:center;font-family:"Arimo",sans-serif;font-size:11px;color:var(--white)}
.main-nav .active{background:linear-gradient(#c4dd3c,var(--lime-dark));border-radius:11px;padding:4px 9px;margin-right:-8px}

/* hero */
.hero{left:0;top:70px;width:1075px;height:369px;background:radial-gradient(ellipse at 40% 40%,var(--sky-light),var(--sky) 70%)}
.hero-title{left:134px;top:136px;font-family:"Bree Serif",serif;color:var(--navy);line-height:1}
.hero-title .pre{font-size:25px;color:var(--white);display:block;margin-bottom:4px}
.hero-title .big{font-size:40px;display:block;line-height:38px}
.hero-copy{left:134px;top:253px;width:335px;font-family:"Bree Serif",serif;font-size:14px;line-height:17.6px;color:var(--white)}
.collage{left:242px;top:10px;width:212px;height:116px;background:linear-gradient(135deg,#e8e2dc,#b9a79b);transform:rotate(-5deg);border:4px solid #fff}
.collage-2{left:268px;top:86px;width:90px;height:60px;background:linear-gradient(#d5d5d5,#8c8c8c);border:3px solid #fff}
.gold-frame{left:352px;top:78px;width:198px;height:150px;border:10px solid #c49a38;background:#2a1722;transform:rotate(-2deg)}
.showcase{left:487px;top:27px;width:455px;height:326px;background:#fff;padding:6px}
.showcase-fill{width:100%;height:100%;background:linear-gradient(110deg,#2b1b24 0 12%,#f4f2f2 12% 50%,#bdbdbd 70%,#555 100%)}
.tab{left:1041px;width:34px;border-radius:5px 0 0 5px;color:var(--white);font-family:"Arimo",sans-serif;font-weight:700;font-size:14px;writing-mode:vertical-rl;transform:rotate(180deg);display:flex;align-items:center;justify-content:center}
.tab-touch{top:76px;height:142px;background:linear-gradient(90deg,var(--orange-light),var(--orange))}
.tab-share{top:235px;height:85px;background:linear-gradient(90deg,#c6dc3a,var(--lime-dark))}

/* call to action band */
.cta-band{left:0;top:439px;width:1075px;height:71px;background:linear-gradient(#3a3a3a,#262626)}
.cta-line{left:0;top:510px;width:1075px;height:4px;background:var(--lime)}
.cta-text{left:140px;top:453px;font-family:"Bree Serif",serif;font-size:17px;line-height:20px;color:var(--white)}
.cta-arrow{left:460px;top:470px}
.btn{height:40px;border-radius:20px;font-family:"Bree Serif",serif;font-size:15px;display:flex;align-items:center;justify-content:center;top:454px}
.btn-price{left:539px;width:136px;background:linear-gradient(var(--orange-light),var(--orange));color:var(--white);box-shadow:0 2px 3px rgba(0,0,0,.4)}
.btn-themes{left:710px;width:225px;background:linear-gradient(#fff,#dcdcdc);color:var(--navy);box-shadow:0 2px 3px rgba(0,0,0,.4)}
.quote-tab{left:748px;top:514px;width:143px;height:31px;background:linear-gradient(#c2d93a,var(--lime-dark));color:#2d3a05;font-family:"Arimo",sans-serif;font-weight:700;font-size:14px;display:flex;align-items:center;justify-content:center;box-shadow:0 2px 3px rgba(0,0,0,.25)}

/* social */
.social{top:530px;width:140px;text-align:center}
.social-name{font-family:"Bree Serif",serif;font-size:25px;color:var(--link);display:flex;align-items:center;justify-content:center;gap:6px;height:34px}
.social-name .dot{width:20px;height:20px;background:var(--link);border-radius:4px}
.social-link{font-family:"Bree Serif",serif;font-size:10px;color:var(--link);margin-top:7px}

/* features */
.features{left:130px;top:610px;width:815px;height:212px;background:var(--white);border:1px solid var(--line);border-radius:6px}
.feature{top:627px;width:246px}
.feature-head{height:50px;border-radius:25px 0 0 25px;background:repeating-linear-gradient(45deg,#e9e9e9 0 2px,#f3f3f3 2px 4px);display:flex;align-items:center;gap:10px;padding-left:10px}
.feature-icon{width:32px;height:32px;border-radius:50%;background:#2c2c2c;display:flex;align-items:center;justify-content:center}
.feature-title{font-size:19px;color:#333;line-height:20px}
.feature-sub{font-size:9px;color:var(--muted);font-weight:300}
.feature-body{font-size:10px;line-height:15px;color:var(--muted);font-weight:300;padding:13px 10px 0 10px}
.feature-body em{font-size:11px}
.ticks li{display:flex;align-items:center;gap:8px;font-size:12px;line-height:18.5px;color:var(--muted)}
.tick{width:12px;height:12px;border-radius:50%;background:#7fb31e;display:flex;align-items:center;justify-content:center}
.testimonial{font-style:italic;padding-left:32px;position:relative}
.testimonial .qmark{position:absolute;left:10px;top:2px;font-family:"Bree Serif",serif;font-size:28px;color:#ccc;font-style:normal}
.testimonial cite{display:block;text-align:right;color:var(--link);margin-top:6px;font-size:10px}

/* recent work */
.work{left:0;top:845px;width:1075px;height:141px;background:#f7f7f7;border-top:1px solid #e2e2e2;border-bottom:1px solid #e2e2e2}
.work-divider{left:254px;top:845px;width:1px;height:141px;background:#ddd}
.work-title{left:140px;top:878px;width:96px;text-align:right}
.work-title h3{font-family:"Bree Serif",serif;font-weight:400;font-size:14px;color:#333}
.work-title p{font-size:9px;line-height:12.5px;color:#666;margin-top:6px}
.thumb{top:870px;width:120px;height:87px;background:#fff;border:1px solid #e2e2e2;border-radius:4px;padding:5px}
.thumb div{width:100%;height:100%}
.nav-arrow{top:905px;font-size:14px;color:#aaa}

/* footer */
.footer-col{top:998px}
.footer-col h4{font-family:"Bree Serif",serif;font-weight:400;font-size:12px;color:#333;margin-bottom:6px}
.footer-col li{font-size:10.5px;line-height:16.8px;color:#222;display:flex;align-items:center;gap:6px}
.footer-col li::before{content:"";width:4px;height:4px;border-radius:50%;background:#222}
.footer-col li.current{color:var(--link)}
.footer-rule{top:987px;width:1px;height:168px;background:#e0e0e0}
.footer-brand{left:745px;top:1006px}
.footer-brand .mark{display:flex;align-items:center;gap:7px;font-family:"Arimo",sans-serif;font-weight:700;font-size:25px;color:#c4c4c4}
.footer-brand .mark span{width:28px;height:28px;background:#c4c4c4}
.footer-brand address{font-style:normal;font-family:"Bree Serif",serif;font-size:11px;line-height:17px;color:#222;margin-top:15px}

/* cookie notice */
.cookie-base{left:0;top:1157px;width:1075px;height:43px;background:#d6d6d6}
.cookie-bar{left:126px;top:1163px;width:823px;height:37px;background:#333;border-radius:3px 3px 0 0;display:flex;align-items:center;padding-left:31px;font-family:"Arimo",sans-serif;font-size:10px;color:#ddd}
.cookie-dismiss{margin-left:19px;width:78px;height:20px;border-radius:10px;background:linear-gradient(var(--orange-light),var(--orange));color:#fff;font-family:"Bree Serif",serif;font-size:11px;display:flex;align-items:center;justify-content:center}
.cookie-more{margin-left:19px;color:#fff;text-decoration:underline}
</style>
</head>
<body>

<header class="site-header abs">
  <div class="brand abs"><span class="brand-square"></span><span class="brand-name">TOVEN</span></div>
  <nav class="main-nav abs">
    <span class="active">HOME</span><span>ABOUT US</span><span>SERVICES</span><span>TECHNOLOGY</span><span>PORTFOLIO</span><span>MEET THE TEAM</span><span>CONTACT US</span>
  </nav>
</header>

<section class="hero abs">
  <h1 class="hero-title abs"><span class="pre">We do</span><span class="big">Web</span><span class="big">Design</span></h1>
  <p class="hero-copy abs">To us, function and form go together like milk and cookies. Yum! Our websites are not only intuitive and user friendly, they're also sleek and beautifully designed. Now that's a delicious combination!</p>
  <div class="collage abs" role="img" aria-label="Strip of portrait photographs"></div>
  <div class="collage-2 abs" role="img" aria-label="Black and white portrait photograph"></div>
  <div class="gold-frame abs" role="img" aria-label="Ornate gold picture frame with script lettering"></div>
  <div class="showcase abs"><div class="showcase-fill" role="img" aria-label="Screenshot of an actress portfolio website with photographs"></div></div>
</section>
<div class="tab tab-touch abs">Get in touch</div>
<div class="tab tab-share abs">Share</div>

<section class="cta-band abs"></section>
<p class="cta-text abs">Start building powerful, professional,<br>easy to use websites and online stores</p>
<svg class="cta-arrow abs" width="62" height="20" viewBox="0 0 62 20"><path d="M2 6 Q28 20 58 10" fill="none" stroke="#fff" stroke-width="1.5"/><path d="M50 6 L58 10 L51 15" fill="none" stroke="#fff" stroke-width="1.5"/></svg>
<div class="btn btn-price abs">VIEW PRICE</div>
<div class="btn btn-themes abs">CHECK OUT OUR THEMES</div>
<div class="cta-line abs"></div>
<div class="quote-tab abs">Get A Quote</div>

<div class="social abs" style="left:125px"><div class="social-name">Friendline</div><p class="social-link">Like Us On Friendline</p></div>
<div class="social abs" style="left:293px"><div class="social-name">Chirper</div><p class="social-link">Follow Us On Chirper</p></div>
<div class="social abs" style="left:452px"><div class="social-name">ProLink</div><p class="social-link">Join Us On ProLink</p></div>
<div class="social abs" style="left:604px"><div class="social-name"><span class="dot"></span>Journo</div><p class="social-link">Read Our Blog</p></div>

<section class="features abs"></section>
<article class="feature abs" style="left:146px">
  <div class="feature-head">
    <div class="feature-icon"><svg width="18" height="14" viewBox="0 0 18 14"><circle cx="9" cy="4" r="3" fill="#fff"/><path d="M3 13 Q9 5 15 13Z" fill="#fff"/><circle cx="3.5" cy="5" r="2" fill="#fff"/><circle cx="14.5" cy="5" r="2" fill="#fff"/></svg></div>
    <div><div class="feature-title">Hello.</div><div class="feature-sub">We are website production team.</div></div>
  </div>
  <p class="feature-body">There are many variations of passages of Lorem Ipsum available, but the majority have suffered alteration in some form, by injected humour, or randomised words which don't look even slightly believable. If you are going to use a passage of Ipsum, you need to be sure there isn't anything embarrassing hidden in the middle of text.</p>
</article>
<article class="feature abs" style="left:410px">
  <div class="feature-head">
    <div class="feature-icon"><svg width="16" height="16" viewBox="0 0 16 16"><rect x="1" y="7" width="8" height="4" rx="2" transform="rotate(-45 5 9)" fill="none" stroke="#fff" stroke-width="1.6"/><rect x="7" y="5" width="8" height="4" rx="2" transform="rotate(-45 11 7)" fill="none" stroke="#fff" stroke-width="1.6"/></svg></div>
    <div><div class="feature-title">We Care</div><div class="feature-sub">High level customer care</div></div>
  </div>
  <div class="feature-body" style="padding-top:10px">
    <em>Because its the little things that matters!</em>
    <p style="margin:6px 0 7px">There are many variations of passages of Lorem Ipsum available,</p>
    <ul class="ticks">
      <li><span class="tick"><svg width="8" height="8" viewBox="0 0 8 8"><path d="M1 4 L3 6 L7 1.5" fill="none" stroke="#fff" stroke-width="1.5"/></svg></span>Cost Effective</li>
      <li><span class="tick"><svg width="8" height="8" viewBox="0 0 8 8"><path d="M1 4 L3 6 L7 1.5" fill="none" stroke="#fff" stroke-width="1.5"/></svg></span>Quick Turnarounds</li>
      <li><span class="tick"><svg width="8" height="8" viewBox="0 0 8 8"><path d="M1 4 L3 6 L7 1.5" fill="none" stroke="#fff" stroke-width="1.5"/></svg></span>Satisfaction Guaranteed</li>
    </ul>
  </div>
</article>
<article class="feature abs" style="left:674px">
  <div class="feature-head">
    <div class="feature-icon"><svg width="16" height="16" viewBox="0 0 16 16"><path d="M4 2 H12 V6 Q12 10 8 10 Q4 10 4 6Z" fill="#fff"/><rect x="7" y="10" width="2" height="3" fill="#fff"/><rect x="5" y="13" width="6" height="1.5" fill="#fff"/></svg></div>
    <div><div class="feature-title">Recommended</div><div class="feature-sub">We have happy clients</div></div>
  </div>
  <blockquote class="feature-body testimonial" style="padding-top:12px"><span class="qmark">&ldquo;</span>TM have used a number of programmers over the years and Rajan and the team are definitely in the top league. I have no problem writing a recommendation for them, they are , efficient have an eye for detail and have delivered ahead of deadline on every job.<cite>— Owen Hartley, Kestrel Studio, Australia</cite></blockquote>
</article>

<section class="work abs"></section>
<div class="work-divider abs"></div>
<div class="work-title abs"><h3>Recent Work</h3><p>Duis ligula massa consectetur a tincidunt pulvinar</p></div>
<span class="nav-arrow abs" style="left:266px">&lsaquo;</span>
<div class="thumb abs" style="left:282px"><div role="img" aria-label="Children's website screenshot" style="background:linear-gradient(#9bc7e0,#7bb84a)"></div></div>
<div class="thumb abs" style="left:413px"><div role="img" aria-label="Printing company website screenshot" style="background:linear-gradient(#e9eef5 0 20%,#2a1e5c 20% 70%,#e9eef5 70%)"></div></div>
<div class="thumb abs" style="left:544px"><div role="img" aria-label="Dark themed website screenshot" style="background:linear-gradient(#1d1d1d,#3a3a3a)"></div></div>
<div class="thumb abs" style="left:675px"><div role="img" aria-label="Family business website screenshot" style="background:linear-gradient(#f1ede4,#c9b08a)"></div></div>
<div class="thumb abs" style="left:806px"><div role="img" aria-label="Blue company website screenshot" style="background:linear-gradient(#2c74c4,#dfeaf7)"></div></div>
<span class="nav-arrow abs" style="left:937px">&rsaquo;</span>

<div class="footer-rule abs" style="left:363px"></div>
<div class="footer-rule abs" style="left:538px"></div>
<div class="footer-rule abs" style="left:699px"></div>
<nav class="footer-col abs" style="left:142px"><h4>SERVICES</h4><ul><li class="current">Web Design</li><li>Graphic Design</li><li>Logo Design</li><li>Web Application</li><li>Content management System (CMS)</li></ul></nav>
<nav class="footer-col abs" style="left:403px"><h4>USEFUL LINKS</h4><ul><li>Home</li><li>About Us</li><li>Services</li><li>Technology</li><li>Portfolio</li><li>Meet the Team</li><li>Contact Us</li></ul></nav>
<nav class="footer-col abs" style="left:580px"><h4>OUR WORK</h4><ul><li>Sports</li><li>Media</li><li>Financial</li><li>Other Sector</li></ul></nav>
<div class="footer-brand abs">
  <div class="mark"><span></span>TOVEN</div>
  <address>FEEL FREE TO CONTACT US<br>123456 Street Name, England &amp; Wales<br>Phone: 05071948</address>
</div>

<div class="cookie-base abs"></div>
<div class="cookie-bar abs">We'd like to set optional cookies to make your user experience better, by using this site you give your consent for us to do this.<span class="cookie-dismiss">Dismiss</span><span class="cookie-more">What are cookies?</span></div>

</body>
</html>
```